2 Page Brochure - Commercial Roofing Company

We are looking for a double sided brochure, full color, for our commercial roofing company that tells customers a little bit about the company, what we do, and shows a few pictures.
The brochure would need to have our logo and color scheme that coordinates with that logo.
I have uploaded our logo, some ideas I had, and then the idea list also has our website on there if you'd like to take a look around there for some more ideas.
I have also uploaded some photos we'd like to use.
Page size should be 8.5" x 11".
Target Market(s)
Commercial Property Owners
Other font styles liked:
- Match logo font ideally so it's cohesive, but whatever looks best
Look and feel

```html
<!DOCTYPE html>
<html lang="en">
<head>
<meta charset="utf-8">
<title>Sunridge Roofing Brochure</title>
<link href="https://fonts.googleapis.com/css2?family=Roboto:wght@400;500;700;900&display=swap" rel="stylesheet">
<style>
:root{
  --peach:#fcc9aa;
  --orange:#e85d22;
  --orange-soft:#ee7a45;
  --dark:#242424;
  --white:#ffffff;
  --badge:#3a3a3a;
  --ink:#1d1d1d;
}
*{box-sizing:border-box;margin:0;padding:0}
html,body{width:1200px;height:775px;overflow:hidden;background:var(--peach);font-family:"Roboto",Arial,sans-serif}
.sheet{position:absolute;top:19px;width:570px;height:739px;overflow:hidden;background:var(--dark)}
.sheet--front{left:20px}
.sheet--back{left:612px}
.hero{position:absolute;left:0;top:0;width:570px;height:380px}
.hero--front{background:linear-gradient(160deg,#8f9a64 0%,#c99a73 30%,#d9ab8a 55%,#c2c3c8 75%,#d6a07c 100%)}
.hero--back{background:linear-gradient(175deg,#5d9be0 0%,#d8dde2 25%,#cfd4d8 36%,#4f7570 48%,#6f9a8d 75%,#8fb2a3 100%)}
.shape{position:absolute;left:0;top:0;width:570px;height:739px}
.brand{position:absolute;left:0;top:28px;width:260px;text-align:center;color:var(--ink)}
.brand__name{font-weight:900;font-size:30px;line-height:1;letter-spacing:.5px;color:var(--ink)}
.brand__sub{font-weight:700;font-size:10.5px;margin-top:18px;letter-spacing:.1px}
.brand__roc{font-weight:700;font-size:12px;margin-top:2px}
.badge{position:absolute;left:33px;top:291px;width:58px;height:58px;border-radius:4px;background:var(--badge)}
.headline{position:absolute;left:32px;top:362px;color:var(--orange);font-weight:700;font-size:23.5px;line-height:26px;text-transform:uppercase}
.story{position:absolute;left:32px;top:454px;width:366px;color:var(--white);font-size:9.6px;line-height:14px}
.story p{margin-bottom:11px}
.photo-ring{position:absolute;border-radius:50%;background:var(--orange-soft);padding:7px}
.photo-ring span{display:block;width:100%;height:100%;border-radius:50%}
.ring-1{left:405px;top:255px;width:132px;height:132px}
.ring-1 span{background:linear-gradient(180deg,#7ea7d6 0%,#6b5249 45%,#7f8284 65%,#9a9a98 100%)}
.ring-2{left:412px;top:397px;width:132px;height:132px}
.ring-2 span{background:linear-gradient(180deg,#6d9ad4 0%,#a48f74 30%,#e6e6e2 55%,#d9d9d4 100%)}
.ring-3{left:412px;top:541px;width:132px;height:132px}
.ring-3 span{background:linear-gradient(180deg,#4d8ed9 0%,#c9cdd0 35%,#7aa095 60%,#5f857b 100%)}
.footer{position:absolute;left:0;top:687px;width:570px;height:52px;background:var(--orange);display:flex;align-items:center;justify-content:space-between;padding:0 36px 0 32px;color:var(--white);font-weight:700;font-size:14px}
.footer__item{display:flex;align-items:center;gap:8px}
.footer__roc{font-size:12.5px}
.footer svg{width:18px;height:18px}
.col-title{position:absolute;color:var(--orange);font-weight:700;font-size:18px;line-height:19px;text-transform:uppercase}
.ticks{position:absolute;list-style:none;color:var(--white);font-size:13px}
.ticks li{display:flex;align-items:flex-start;gap:10px;height:22px}
.ticks svg{width:16px;height:16px;flex:none;margin-top:-1px}
.services{position:absolute;left:345px;top:444px;list-style:none;color:var(--white);font-weight:700;font-size:15px;line-height:20px}
.services li{display:flex;gap:14px;margin-bottom:10px}
.services svg{width:20px;height:20px;flex:none}
.divider{position:absolute;left:330px;top:336px;height:350px;border-left:1.5px dashed var(--orange)}
.area{position:absolute;left:32px;top:659px;color:var(--white);font-size:13px}
</style>
</head>
<body>
<svg width="0" height="0" style="position:absolute">
  <symbol id="tick" viewBox="0 0 20 20"><path d="M17 9.5A7.5 7.5 0 1 1 13 3.2" fill="none" stroke="#e85d22" stroke-width="1.8" stroke-linecap="round"/><path d="M6 9.5l3.2 3.2L18 4" fill="none" stroke="#e85d22" stroke-width="1.8" stroke-linecap="round" stroke-linejoin="round"/></symbol>
  <symbol id="phone" viewBox="0 0 20 20"><circle cx="10" cy="10" r="10" fill="#fff"/><path d="M6.5 5l2 2-1 1.5c.7 1.6 2 2.9 3.5 3.6l1.5-1 2 2-1.2 1.6C9.5 14.5 5.5 10.5 5.2 6.3z" fill="#e85d22"/></symbol>
  <symbol id="globe" viewBox="0 0 20 20"><circle cx="10" cy="10" r="10" fill="#fff"/><circle cx="10" cy="10" r="6" fill="none" stroke="#e85d22" stroke-width="1.3"/><ellipse cx="10" cy="10" rx="2.6" ry="6" fill="none" stroke="#e85d22" stroke-width="1.1"/><path d="M4 10h12M5 7h10M5 13h10" stroke="#e85d22" stroke-width="1"/></symbol>
</svg>

<section class="sheet sheet--front">
  <div class="hero hero--front" role="img" aria-label="Photo of a flat commercial roof with solar panels and desert hills behind"></div>
  <svg class="shape" viewBox="0 0 570 739">
    <path d="M0 293 C80 262 200 262 300 300 C360 322 400 352 440 362 C490 372 540 350 570 333 L570 739 L0 739Z" fill="#e85d22"/>
    <path d="M0 308 C80 278 200 278 300 314 C360 336 400 366 440 376 C490 384 540 360 570 346 L570 739 L0 739Z" fill="#242424"/>
    <path d="M0 0 L302 0 C300 80 230 140 110 145 C60 146 25 140 0 130Z" fill="#e85d22"/>
    <path d="M0 0 L294 0 C290 75 222 133 110 137 C60 138 25 132 0 122Z" fill="#fff"/>
  </svg>
  <div class="brand">
    <div class="brand__name">SUNRIDGE<br>ROOFING</div>
    <div class="brand__sub">OUR SPECIALTY IS COMMERCIAL ROOFS</div>
    <div class="brand__roc">AZ ROC 512870</div>
  </div>
  <div class="badge" role="img" aria-label="Contractor certification badge"></div>
  <h1 class="headline">Installing<br>roofs across<br>Arizona since 1984</h1>
  <div class="story">
    <p>Sunridge Roofing opened the doors in 1984, and we’ve since installed, serviced, maintained, and coated thousands of commercial roofs around the state of Arizona, in the many climate regions of the state.</p>
    <p>Though we all live here for the constant sunshine, Arizona is one of the harshest environments in the US for roofs. Constant sun, heat, dryness, and then the torrential monsoon downpours all test the limits of your roof.</p>
    <p>We work with you to come up with a solution that works for your roof and will keep your business dry for years to come. Then, our team of project managers, superintendents, foremen, and field workers all come together to execute on that plan and install a quality roof.</p>
    <p>We are certified with many different manufacturers, so we’re able to offer custom solutions to solve your issues, that will also often come with reputable manufacturer warranties.</p>
  </div>
  <div class="photo-ring ring-1"><span role="img" aria-label="Photo of a finished commercial building with a work truck"></span></div>
  <div class="photo-ring ring-2"><span role="img" aria-label="Photo of a white membrane roof with parapet and ladder"></span></div>
  <div class="photo-ring ring-3"><span role="img" aria-label="Photo of a green standing seam metal roof on a restaurant"></span></div>
  <footer class="footer">
    <span class="footer__item"><svg><use href="#phone"/></svg>480-555-0142</span>
    <span class="footer__roc">AZ ROC 512870</span>
    <span class="footer__item"><svg><use href="#globe"/></svg>www.sunridge-roofing.com</span>
  </footer>
</section>

<section class="sheet sheet--back">
  <div class="hero hero--back" role="img" aria-label="Photo of a green standing seam metal roof below a restaurant sign"></div>
  <svg class="shape" viewBox="0 0 570 739">
    <path d="M0 255 C40 232 120 225 220 248 C320 272 380 330 440 334 C500 338 540 318 570 300 L570 739 L0 739Z" fill="#e85d22"/>
    <path d="M0 270 C40 245 120 240 220 262 C320 288 380 346 440 350 C500 352 540 334 570 318 L570 739 L0 739Z" fill="#242424"/>
    <path d="M0 0 L302 0 C300 80 230 140 110 145 C60 146 25 140 0 130Z" fill="#e85d22"/>
    <path d="M0 0 L294 0 C290 75 222 133 110 137 C60 138 25 132 0 122Z" fill="#fff"/>
  </svg>
  <div class="brand">
    <div class="brand__name">SUNRIDGE<br>ROOFING</div>
    <div class="brand__sub">OUR SPECIALTY IS COMMERCIAL ROOFS</div>
    <div class="brand__roc">AZ ROC 512870</div>
  </div>

  <h2 class="col-title" style="left:32px;top:292px">Certified with the<br>following manufacturers:</h2>
  <ul class="ticks" style="left:32px;top:349px">
    <li><svg><use href="#tick"/></svg>Apexa</li>
    <li><svg><use href="#tick"/></svg>Stratum</li>
    <li><svg><use href="#tick"/></svg>KR</li>
    <li><svg><use href="#tick"/></svg>Truline</li>
  </ul>
  <ul class="ticks" style="left:134px;top:349px">
    <li><svg><use href="#tick"/></svg>Corvo</li>
    <li><svg><use href="#tick"/></svg>Veltra</li>
    <li><svg><use href="#tick"/></svg>And more</li>
  </ul>

  <h2 class="col-title" style="left:32px;top:444px">Sunridge Roofing installs<br>the following products:</h2>
  <ul class="ticks" style="left:32px;top:502px">
    <li><svg><use href="#tick"/></svg>TPO</li>
    <li><svg><use href="#tick"/></svg>PVC</li>
    <li><svg><use href="#tick"/></svg>Modified Bitumen</li>
    <li><svg><use href="#tick"/></svg>Silicone Coatings</li>
    <li><svg><use href="#tick"/></svg>Acrylic Coatings</li>
  </ul>
  <ul class="ticks" style="left:178px;top:501px">
    <li><svg><use href="#tick"/></svg>Shingle</li>
    <li><svg><use href="#tick"/></svg>Metal</li>
    <li><svg><use href="#tick"/></svg>Tile</li>
    <li style="height:40px;line-height:18px"><svg><use href="#tick"/></svg>Spray Polyurethane<br>Foam</li>
    <li><svg><use href="#tick"/></svg>And more</li>
  </ul>

  <h2 class="col-title" style="left:32px;top:630px">Service area:</h2>
  <p class="area">We service the entire state of Arizona.</p>

  <div class="divider"></div>

  <h2 class="col-title" style="left:340px;top:362px;width:215px;text-align:center;font-size:17px">Sunridge Roofing offers the following services:</h2>
  <ul class="services">
    <li><svg><use href="#tick"/></svg>New Roof Installation</li>
    <li><svg><use href="#tick"/></svg>Re-roofing</li>
    <li><svg><use href="#tick"/></svg>Roof Maintenance and<br>Service</li>
    <li><svg><use href="#tick"/></svg>Roof Inspections</li>
    <li><svg><use href="#tick"/></svg>Roof Coatings</li>
    <li><svg><use href="#tick"/></svg>And more</li>
  </ul>

  <footer class="footer">
    <span class="footer__item"><svg><use href="#phone"/></svg>480-555-0142</span>
    <span class="footer__roc">AZ ROC 512870</span>
    <span class="footer__item"><svg><use href="#globe"/></svg>www.sunridge-roofing.com</span>
  </footer>
</section>
</body>
</html>
```